High end Electrical/home automation Business Card

Need a card for a high end electrical and home automation company utilising the existing logo.
Phone
Email
Website

Like black look with raised detail. Don’t necessarily need to keep colour of logo it could be made grayscale or white etc

Target Market(s)

High end clients

Contact Information for Business Card

Ridgeline Electrical

Requirements
Must have
• Logo, phone, email, website, address

High end look
Nice to have
• Black background card
Raised font
Should not have
• Lots of colour

```html
<!DOCTYPE html>
<html lang="en">
<head>
<meta charset="utf-8">
<title>Ridgeline Electrical — Business Card</title>
<link rel="stylesheet" href="https://fonts.googleapis.com/css2?family=Montserrat:wght@500;600;700&family=Open+Sans:wght@400;600&display=swap">
<style>
  :root {
    --backdrop: #3b3b3d;
    --card: #2e2e30;
    --ink: #aaaaab;
    --ink-soft: #9a9a9b;
    --rule: #8e8e90;
    --highlight: rgba(255,255,255,0.18);
    --depth: rgba(0,0,0,0.55);
  }
  * { box-sizing: border-box; margin: 0; padding: 0; }
  html, body { width: 1200px; height: 1077px; overflow: hidden; }
  body {
    background: var(--backdrop);
    font-family: "Open Sans", sans-serif;
    position: relative;
  }
  .card {
    position: absolute;
    left: 170px;
    width: 860px;
    height: 490px;
    background: var(--card);
    box-shadow: 0 10px 30px rgba(0,0,0,0.45);
  }
  .card--front { top: 32px; }
  .card--back { top: 555px; }

  .raised {
    text-shadow: -1px -1px 0 var(--highlight), 2px 2px 2px var(--depth);
  }

  /* Front face */
  .front-brand {
    position: absolute;
    inset: 0;
    display: flex;
    align-items: center;
    justify-content: center;
    gap: 22px;
  }
  .brand-dot {
    width: 34px; height: 34px;
    border-radius: 50%;
    background: var(--ink);
  }
  .brand-name {
    font-family: "Montserrat", sans-serif;
    font-weight: 700;
    color: var(--ink);
    letter-spacing: 0.5px;
  }
  .front-brand .brand-name { font-size: 54px; }

  /* Back face */
  .back-brand {
    position: absolute;
    left: 50px;
    top: 0;
    width: 250px;
    height: 100%;
    display: flex;
    flex-direction: column;
    align-items: center;
    justify-content: center;
    gap: 18px;
    text-align: center;
  }
  .back-brand .brand-name { font-size: 36px; line-height: 1.15; }
  .divider {
    position: absolute;
    left: 330px;
    top: 60px;
    width: 2px;
    height: 370px;
    background: var(--rule);
  }
  .contact {
    position: absolute;
    left: 390px;
    top: 95px;
    right: 40px;
  }
  .person-name {
    font-family: "Montserrat", sans-serif;
    font-weight: 600;
    font-size: 40px;
    letter-spacing: 1.5px;
    color: var(--ink);
    text-transform: uppercase;
  }
  .person-title {
    font-size: 25px;
    color: var(--ink-soft);
    letter-spacing: 0.8px;
    margin-top: 2px;
  }
  .contact-list {
    list-style: none;
    margin-top: 48px;
  }
  .contact-list li {
    display: flex;
    align-items: center;
    gap: 16px;
    font-size: 28px;
    color: var(--ink);
    letter-spacing: 0.6px;
    height: 48px;
  }
  .contact-list svg {
    width: 24px; height: 24px;
    flex: none;
    fill: none;
    stroke: var(--ink);
    stroke-width: 2;
  }
</style>
</head>
<body>

<section class="card card--front" aria-label="Card front">
  <div class="front-brand">
    <span class="brand-dot" aria-hidden="true"></span>
    <span class="brand-name">Ridgeline Electrical</span>
  </div>
</section>

<section class="card card--back" aria-label="Card back">
  <div class="back-brand">
    <span class="brand-dot" aria-hidden="true"></span>
    <span class="brand-name">Ridgeline<br>Electrical</span>
  </div>
  <div class="divider" aria-hidden="true"></div>
  <div class="contact">
    <h1 class="person-name raised">Daniel Harper</h1>
    <p class="person-title raised">Genaral Manager</p>
    <ul class="contact-list">
      <li class="raised">
        <svg viewBox="0 0 24 24" aria-hidden="true"><path d="M5 3h4l2 5-2.5 1.5a11 11 0 0 0 6 6L16 13l5 2v4a2 2 0 0 1-2 2A17 17 0 0 1 3 5a2 2 0 0 1 2-2z"/></svg>
        +243 970 555 218
      </li>
      <li class="raised">
        <svg viewBox="0 0 24 24" aria-hidden="true"><rect x="2" y="5" width="20" height="14"/><path d="M2 5l10 8 10-8"/></svg>
        info@ridgelineelectrical.com
      </li>
      <li class="raised">
        <svg viewBox="0 0 24 24" aria-hidden="true"><circle cx="12" cy="12" r="10"/><path d="M2 12h20M12 2c3 3 3 17 0 20M12 2c-3 3-3 17 0 20"/></svg>
        www.ridgelineelectrical.com
      </li>
    </ul>
  </div>
</section>

</body>
</html>
```